We need a flyer where we promote a workshop to our members of the jewish community www.qvb-gemeinde.example . The workshop is calles "guidance in ten seasons presented by QVB. We would like to see a flyer with the below text is used and also some pictures (attached). The flyer should come over as cool, fresh, innovative for a younger crowd so called young professionals (age 28-35).
TITLE.
"Guidance in Ten Seasons.
SUBTITLE.
Your systematic self-coaching roadmap to power and impact—and your future.”
TEXT.
Dr. Martin K. Halvorsen is the CEO Emeritus of Alpine Advisory Partners—he made an exit in 2013. He is the award-winning author of 8 books, including "Plan-Into-Motion," "Speak or Falter" and "The Cantor and the Chairman.”
For the past 20 years he has taught leadership at Harwick University in New York and at BKU (Lindenberg University) to prepare future CEOs and other leaders in business, government , nonprofits and the military.
Now, in a process exclusively designed for QVB’s next generation of emerging leaders, Martin unpacks his leadership secrets in 3 action-packed labs—reduced to the max:
Lab 1. Guidance in Ten Seasons: The Summit Guide Triangle®. Self-Assessment. Self-Leadership: “The Lantern.” 5-Year Vision. 100-Day Catalytic Project.
Lab 2. Leading Through Language. Relationship: Building Trust. Plan-Into-Motion. Cockpit.
Lab 3. Debrief and Scale-Up. Sustainability. Action Tools.
Do you want to build your own future and a life you love? Do you want to jump-start that future and life over 100 days while learning a toolbox of leadership skills, networking with like-minded people—and even get some pizza? Then join us.
Target Market(s)
young professionals age 28-35

```html
<!DOCTYPE html>
<html lang="en">
<head>
<meta charset="utf-8">
<title>Guidance in Ten Seasons – Workshop Flyer</title>
<link rel="stylesheet" href="https://fonts.googleapis.com/css2?family=Bebas+Neue&family=Oswald:wght@500&family=Open+Sans:ital,wght@0,400;1,400;1,700&display=swap">
<style>
  :root {
    --page-bg: #4a4643;
    --flyer-black: #050505;
    --panel-dark: #0e0b10;
    --brand-red: #d3202a;
    --band-red-dark: #8c0f15;
    --band-red: #c21f28;
    --text-white: #ffffff;
    --text-soft: #ececec;
  }
  * { margin: 0; padding: 0; box-sizing: border-box; }
  html, body { width: 1200px; height: 857px; overflow: hidden; }
  body { background: var(--page-bg); position: relative; }

  .flyer {
    position: absolute; left: 307px; top: 15px;
    width: 586px; height: 826px;
    background: var(--flyer-black);
    overflow: hidden;
    color: var(--text-white);
  }

  .title { position: absolute; font-family: 'Bebas Neue', 'Oswald', sans-serif; line-height: 1; color: var(--text-white); }
  .title-main { left: 20px; top: 56px; font-size: 102px; letter-spacing: 0.5px; }
  .title-in { left: 180px; top: 160px; font-size: 38px; }
  .title-second { left: 20px; top: 214px; font-size: 88px; letter-spacing: 0.5px; }

  .book-cover {
    position: absolute; left: 393px; top: 58px; width: 160px; height: 272px;
    background: linear-gradient(100deg, #b8141c 0%, #d9262d 55%, #9d1218 100%);
    transform: skewY(-4deg);
    box-shadow: 4px 4px 10px rgba(0,0,0,.6);
  }

  .photo-stage {
    position: absolute; left: 0; top: 322px; width: 586px; height: 450px;
    background:
      radial-gradient(ellipse at 28% 55%, #6e6f76 0%, #3a3b44 28%, rgba(20,20,30,0) 55%),
      linear-gradient(180deg, #0b0b12 0%, #1a2150 45%, #1d2a6a 70%, #120f1c 100%);
  }

  .lab-panel {
    position: absolute; left: 300px; top: 614px; right: 0; height: 158px;
    background: var(--panel-dark);
  }

  .info { position: absolute; left: 315px; width: 248px; }
  .subtitle {
    top: 402px; font-family: 'Bebas Neue', 'Oswald', sans-serif;
    font-size: 24px; line-height: 1.04; color: var(--text-white);
  }
  .workshop-name {
    top: 484px; font-family: 'Bebas Neue', 'Oswald', sans-serif;
    font-size: 19px; color: var(--brand-red);
  }
  .presenter {
    top: 503px; font-family: 'Open Sans', sans-serif; font-style: italic; font-weight: 700;
    font-size: 12px;
  }
  .bio {
    top: 526px; font-family: 'Open Sans', sans-serif; font-size: 9.4px; line-height: 11.6px;
    text-align: justify; color: var(--text-soft);
  }
  .bio em { font-style: italic; }

  .labs { top: 648px; list-style: none; }
  .lab { display: flex; gap: 6px; margin-bottom: 9px; }
  .lab-label {
    flex: 0 0 40px; font-family: 'Bebas Neue', 'Oswald', sans-serif; font-size: 16px;
    line-height: 1; color: var(--brand-red); letter-spacing: 0.5px;
  }
  .lab-text { font-family: 'Open Sans', sans-serif; font-size: 9.4px; line-height: 10.8px; color: var(--text-soft); }

  .footer-band {
    position: absolute; left: 0; bottom: 0; width: 586px; height: 54px;
    background: linear-gradient(90deg, var(--band-red-dark), var(--band-red) 50%, var(--band-red-dark));
    display: flex; align-items: center; justify-content: center;
    font-family: 'Oswald', sans-serif; font-weight: 500; font-size: 12.6px; letter-spacing: 0.7px;
    white-space: nowrap; color: var(--text-white);
  }
  .footer-band .sep { margin: 0 8px; }
</style>
</head>
<body>
  <main class="flyer">
    <h1>
      <span class="title title-main">GUIDANCE</span>
      <span class="title title-in">IN</span>
      <span class="title title-second">TEN SEASONS</span>
    </h1>

    <div class="book-cover" role="img" aria-label="Book cover of Guidance in Ten Seasons: red cover with a road leading to the horizon"></div>

    <div class="photo-stage" role="img" aria-label="Portrait of the speaker with arms crossed, in front of a conference stage with an audience"></div>
    <div class="lab-panel"></div>

    <p class="info subtitle">YOUR SYSTEMATIC SELF-COACHING ROADMAP&nbsp; TO POWER AND IMPACT AND YOUR FUTURE</p>
    <p class="info workshop-name">GUIDANCE IN TEN SEASONS</p>
    <p class="info presenter">presented by QVB</p>
    <p class="info bio">Dr. Martin K. Halvorsen is the CEO Emeritus of Alpine Advisory Partners - he made an exit in 2013. He is the award-winning author of 8 books, including <em>“Plan-Into-Motion,” “Speak or Falter”</em> and <em>“The Cantor and the Chairman.”</em> For the past 20 years he has taught leadership at Harwick University in New York and at BKU (Lindenberg University) to prepare future CEOs and other leaders in business, government, nonprofits and the military.</p>

    <ul class="info labs">
      <li class="lab"><span class="lab-label">LAB 1</span><span class="lab-text">Guidance in Ten Seasons: The Summit Guide Triangle®. Self-Assessment. Self-Leadership: “The Lantern.” 5-Year Vision. 100-Day Catalytic Project.</span></li>
      <li class="lab"><span class="lab-label">LAB 2</span><span class="lab-text">Leading Through Language. Relationship: Building Trust. Plan-Into-Motion. Cockpit.</span></li>
      <li class="lab"><span class="lab-label">LAB 3</span><span class="lab-text">Debrief and Scale-Up. Sustainability. Action Tools.</span></li>
    </ul>

    <footer class="footer-band">
      <span>WORKSHOP: QVB EVENTS</span><span class="sep">|</span>
      <span>MARCH 6, 2018, 7:00 P.M. - 9:00 P.M.</span><span class="sep">|</span>
      <span>WWW.QVB-GEMEINDE.EXAMPLE</span>
    </footer>
  </main>
</body>
</html>
```